TK Drafting

Simple Design - Logo is done (from this site). Logo on one side - Back Side an image or outline of a house blue print - My name, phone, email, website url. Prefer the traditional Architectural style of letters -

Target Market(s)

Customers who need a floor plan redesigned for renovations or realtors who want a floor plan for marketing their listings

Industry/Entity Type

Architecture

Contact Information for Business Card

Colby Faust - Name
415-362-8840 - Phone
tkdraftingco@mailpost.example
www.tkdraftingco.example

Font styles to use
Other font styles liked:
• Architecture writing -

Colors
0555a3
3276b5
85acd3

Requirements
Must have
• Logo that is attached. I like an indigo blue color for the background or a royal blue - gray logo OR - white and clean with the logo on one side and the same color gray lettering on the other side
Nice to have
• some sort of image that shows a residential blue print. It may not be possible on this small of a card though.
Should not have
• Nothing cartoonish.

```html
<!DOCTYPE html>
<html lang="en">
<head>
<meta charset="utf-8">
<title>TK Drafting – Business Card</title>
<link rel="stylesheet" href="https://fonts.googleapis.com/css2?family=Open+Sans:wght@400;600;700&display=swap">
<style>
  :root {
    --bg: #2b2d31;
    --card-blue: #0756a6;
    --card-blue-deep: #044b95;
    --mark-faint: #1d4fb8;
    --mark-gray: #b8bbc2;
    --text-light: #dfe3ea;
  }
  * { box-sizing: border-box; margin: 0; padding: 0; }
  html, body {
    width: 1200px;
    height: 913px;
    overflow: hidden;
    background: var(--bg);
    font-family: "Open Sans", Arial, sans-serif;
  }
  .canvas {
    position: relative;
    width: 1200px;
    height: 913px;
  }
  .card {
    position: absolute;
    width: 620px;
    height: 354px;
    border-radius: 22px;
    background: var(--card-blue);
    box-shadow: 0 14px 30px rgba(0,0,0,0.45);
    overflow: hidden;
  }
  .card--front { left: 110px; top: 70px; }
  .card--back  { left: 470px; top: 489px; }

  .brand {
    position: absolute;
    display: flex;
    align-items: center;
    gap: 12px;
    font-weight: 600;
    white-space: nowrap;
  }
  .brand__square {
    width: 22px;
    height: 22px;
    background: currentColor;
  }
  .card--front .brand {
    left: 50%;
    top: 50%;
    transform: translate(-50%, -50%);
    font-size: 44px;
    color: var(--mark-faint);
  }
  .card--back .brand {
    right: 40px;
    top: 62px;
    font-size: 32px;
    color: var(--mark-gray);
  }
  .brand__square--small { width: 18px; height: 18px; }

  .contact {
    position: absolute;
    left: 54px;
    bottom: 44px;
    color: var(--text-light);
  }
  .contact__name {
    font-weight: 700;
    font-size: 22px;
    letter-spacing: 0.5px;
    color: var(--mark-gray);
    text-transform: uppercase;
    margin-bottom: 14px;
  }
  .contact__list { list-style: none; }
  .contact__item {
    display: flex;
    align-items: center;
    gap: 9px;
    font-size: 17px;
    line-height: 27px;
  }
  .contact__icon { width: 14px; height: 14px; flex: none; }
</style>
</head>
<body>
<main class="canvas">
  <section class="card card--front" aria-label="Card front">
    <div class="brand"><span class="brand__square"></span>TK Drafting</div>
  </section>

  <section class="card card--back" aria-label="Card back">
    <div class="brand"><span class="brand__square brand__square--small"></span>TK Drafting</div>

    <div class="contact">
      <p class="contact__name">Colby Faust</p>
      <ul class="contact__list">
        <li class="contact__item">
          <svg class="contact__icon" viewBox="0 0 16 16" aria-hidden="true"><path fill="#dfe3ea" d="M3.5 1.5l2.2 2.8-1.3 1.6c.9 2 2.6 3.7 4.7 4.7l1.6-1.3 2.8 2.2-1.4 2.5C7 13.6 2.4 9 1 3z"/></svg>
          415-362-8840
        </li>
        <li class="contact__item">
          <svg class="contact__icon" viewBox="0 0 16 16" aria-hidden="true"><rect x="1" y="3" width="14" height="10" fill="#dfe3ea"/><path d="M1 3l7 6 7-6" fill="none" stroke="#0756a6" stroke-width="1.4"/></svg>
          tkdraftingco@mailpost.example
        </li>
        <li class="contact__item">
          <svg class="contact__icon" viewBox="0 0 16 16" aria-hidden="true"><circle cx="8" cy="8" r="7" fill="#dfe3ea"/><path d="M1 8h14M8 1c-3 3-3 11 0 14M8 1c3 3 3 11 0 14" fill="none" stroke="#0756a6" stroke-width="1.1"/></svg>
          www.tkdraftingco.example
        </li>
      </ul>
    </div>
  </section>
</main>
</body>
</html>
```